Investment company needing business card

We are wanting a business card which looks sharp and easy on the eye. We are thinking of having a business card with the logo embossed on it, to really make it stand out. We will only have a small amount of information of the business card, person's name, position, email address and phone number

Contact Information for Business Card

Danica Pruett
Executive Assistant
+64 21 547 3162
danicap@harwellcapital.co.nz

Requirements
Must have
• Embossed logo
Should not have
• Not to be busy

```html
<!DOCTYPE html>
<html lang="en">
<head>
<meta charset="utf-8">
<title>Harwell Capital – Business Card</title>
<link href="https://fonts.googleapis.com/css2?family=Arimo:wght@400;700&display=swap" rel="stylesheet">
<style>
  :root {
    --backdrop: #141517;
    --card-front: #e4e4e4;
    --card-back: #0e0e0e;
    --brand-green: #20a56a;
    --ink-grey: #4a4a4c;
    --rule-grey: #6a6a6a;
    --emboss-dark: #050505;
  }
  * { margin: 0; padding: 0; box-sizing: border-box; }
  html, body {
    width: 1200px; height: 965px; overflow: hidden;
    background: var(--backdrop);
    font-family: "Arimo", Arial, sans-serif;
  }
  .card {
    position: absolute; left: 277px; width: 648px; height: 369px;
    box-shadow: 0 4px 14px rgba(0,0,0,0.5);
  }
  .card--front { top: 97px; background: var(--card-front); }
  .card--back { top: 504px; background: var(--card-back); }

  .brand { position: absolute; display: flex; align-items: center; gap: 16px; }
  .brand__mark { width: 70px; height: 70px; }
  .brand__name { font-weight: 700; font-size: 38px; letter-spacing: 1px; white-space: nowrap; }

  .card--front .brand { left: 35px; top: 54px; }
  .card--front .brand__mark { background: var(--brand-green); }
  .card--front .brand__name { color: var(--brand-green); }

  .card--back .brand { left: 50%; top: 50%; transform: translate(-50%, -50%); }
  .card--back .brand__mark { background: var(--emboss-dark); }
  .card--back .brand__name { color: var(--emboss-dark); }

  .person { position: absolute; left: 34px; top: 232px; }
  .person__name { color: var(--brand-green); font-size: 21px; line-height: 1.1; }
  .person__role { color: var(--ink-grey); font-size: 15px; margin-top: 2px; }

  .divider {
    position: absolute; left: 0; right: 0; top: 284px;
    height: 1px; background: var(--rule-grey);
  }
  .divider__accent {
    position: absolute; left: 35px; top: 2px; width: 164px;
    border-top: 2px dotted var(--brand-green);
  }

  .contact { position: absolute; left: 34px; top: 302px; list-style: none; }
  .contact__item {
    display: flex; align-items: center; gap: 6px;
    color: var(--ink-grey); font-size: 15px; height: 19px;
  }
  .contact__icon { width: 12px; height: 12px; flex: none; }
  .contact__accent { color: var(--brand-green); }
</style>
</head>
<body>
  <section class="card card--front">
    <div class="brand">
      <div class="brand__mark"></div>
      <span class="brand__name">HARWELL CAPITAL</span>
    </div>

    <div class="person">
      <div class="person__name">DANICA PRUETT</div>
      <div class="person__role">Executive Assistant</div>
    </div>

    <div class="divider"><div class="divider__accent"></div></div>

    <ul class="contact">
      <li class="contact__item">
        <svg class="contact__icon" viewBox="0 0 12 12" aria-hidden="true">
          <circle cx="6" cy="6" r="6" fill="#20a56a"/>
          <path d="M4 3.2 L5 4.6 L4.5 5.3 Q5.3 6.8 6.7 7.5 L7.4 7 L8.8 8 L8.2 9 Q5.5 8.8 3.2 4 Z" fill="#e4e4e4"/>
        </svg>
        +64 21 547 3162
      </li>
      <li class="contact__item">
        <svg class="contact__icon" viewBox="0 0 12 12" aria-hidden="true">
          <circle cx="6" cy="6" r="6" fill="#20a56a"/>
          <rect x="3" y="4" width="6" height="4.2" fill="none" stroke="#e4e4e4" stroke-width="0.9"/>
          <path d="M3 4 L6 6.4 L9 4" fill="none" stroke="#e4e4e4" stroke-width="0.9"/>
        </svg>
        <span>danicap@<span class="contact__accent">harwell</span>capital.co.nz</span>
      </li>
    </ul>
  </section>

  <section class="card card--back">
    <div class="brand">
      <div class="brand__mark"></div>
      <span class="brand__name">HARWELL CAPITAL</span>
    </div>
  </section>
</body>
</html>
```